High-End Print/Digital Ad for Unique Luxury Travel Company Required

Objective:
Design a compelling and visually striking advertisement that highlights our company’s unmatched luxury travel experiences. The ad should elevate our brand image, spark curiosity, and drive prospective clients to contact us.
Target Audience:
• Affluent individuals seeking extraordinary, tailor-made travel experiences
• Affluent, luxury, high-net-worth individuals looking for value, expertise, and white-glove service
• Professionals or retirees who appreciate unique, thoughtfully curated travel over mainstream tourism
Key Messages to Communicate:
• One-of-a-kind luxury travel: Once-in-a-lifetime experiences that are curated with creativity and meticulous attention to detail
• Exceptional service: White-glove, personalized planning from start to finish
• 38 years’ travel experience – expert knowledge of destinations, modes of travel, premium accommodations and well-established, meaningful industry connections.
• Highly trusted: Cruise line executives often say, “No one does what you do.”
Tone and Style:
• Elegant, luxurious, sophisticated
• Eye-catching, polished, and modern
• Professional but warm—conveys trust and credibility
• High-impact visuals (full-bleed imagery, custom graphics, or high-end photography)
Deliverables:
• One full-page print ad and digital ad
• Ready-to-print, high-resolution file + working file (PSD, AI, etc.)
Optional: Social media-optimized version or short motion-graphic variation (if designer offers it)
Inspiration & Visual Style Suggestions:
• Think Lumen Voyage, Harlow Pike Wanderer, Seven Harbors, or Velora Retreats ad styles
• Large, emotive imagery with elegant typography
• Clean layout that speaks luxury, clarity, and trust
Copy Direction (draft):
For those who’ve explored the world—and crave something beyond the ordinary.
Each journey is a masterfully curated experience, rich in detail, seamless in execution, and unforgettable in every way.
Founded in 1997, Tidal Reverie is a unique travel company specializing in cruising, all-inclusive luxury properties, and tours world-wide for individuals, groups, and incentives.
We offer an exceptional range of services designed to ensure every journey is flawlessly executed and truly unforgettable.
Let us help you plan your next extraordinary adventure.
Note: You may refine the copy slightly based on layout or format needs.
Other Resources for References:
1. Website - www.tidalreverie-example.com

```html
<!DOCTYPE html>
<html lang="en">
<head>
<meta charset="utf-8">
<title>Tidal Reverie – Luxury Reimagined</title>
<link rel="stylesheet" href="https://fonts.googleapis.com/css2?family=Playfair+Display:wght@400;500&family=Poppins:wght@400;600;700&family=Allura&display=swap">
<style>
  :root {
    --ink-deep: #061522;
    --ocean: #0c3346;
    --lagoon: #1f9c95;
    --shallow: #3cc4b0;
    --canopy: #2f7a2e;
    --canopy-dark: #163e14;
    --sand: #d9c9a8;
    --mint: #45cfa3;
    --cyan: #2fd3e6;
    --white: #ffffff;
  }
  * { margin: 0; padding: 0; box-sizing: border-box; }
  html, body { width: 952px; height: 1200px; overflow: hidden; background: var(--ink-deep); }
  .ad {
    position: relative;
    width: 952px;
    height: 1200px;
    overflow: hidden;
    font-family: "Poppins", sans-serif;
    color: var(--white);
  }
  .ad__photo {
    position: absolute; inset: 0;
    background:
      radial-gradient(ellipse 230px 300px at 600px 680px, rgba(60,196,176,.75), rgba(31,156,149,0) 70%),
      linear-gradient(112deg, var(--ink-deep) 0%, var(--ocean) 38%, var(--lagoon) 56%, var(--sand) 62%, var(--canopy) 66%, var(--canopy-dark) 100%);
  }
  .ad__shade {
    position: absolute; inset: 0;
    background: linear-gradient(90deg, rgba(6,21,34,.85) 0%, rgba(6,21,34,.45) 45%, rgba(6,21,34,0) 65%);
  }
  .headline {
    position: absolute; left: 0; right: 0; top: 96px;
    font-family: "Playfair Display", serif;
    font-weight: 500;
    text-align: center;
    line-height: 1;
  }
  .headline__top { display: block; font-size: 132px; letter-spacing: 1px; padding-left: 10px; }
  .headline__bottom {
    display: block; margin-top: 14px; font-size: 132px; letter-spacing: -1px;
    background: linear-gradient(90deg, #2a9e6e 0%, var(--mint) 40%, var(--cyan) 70%, #3ad9f0 100%);
    -webkit-background-clip: text; background-clip: text; color: transparent;
  }
  .subhead { position: absolute; left: 94px; top: 372px; font-size: 21px; line-height: 1.35; font-weight: 400; }
  .subhead strong { font-weight: 700; }
  .features { position: absolute; left: 94px; top: 518px; width: 300px; }
  .feature { margin-bottom: 28px; }
  .feature__title { font-size: 18.5px; font-weight: 700; color: var(--mint); letter-spacing: .2px; margin-bottom: 6px; }
  .feature__text { font-size: 12.5px; line-height: 1.35; }
  .cta { position: absolute; left: 92px; top: 856px; }
  .cta__script { font-family: "Allura", cursive; font-size: 34px; color: var(--cyan); line-height: 1; }
  .cta__lead { font-size: 16px; font-weight: 700; margin-top: 4px; }
  .contact { position: absolute; left: 94px; top: 944px; font-size: 19px; }
  .contact__row { display: flex; align-items: center; gap: 7px; height: 36px; }
  .contact__icon { width: 17px; height: 17px; }
  .brand { position: absolute; left: 94px; top: 1048px; display: flex; align-items: center; gap: 10px; }
  .brand__mark { width: 34px; height: 34px; border-radius: 50%; background: var(--white); }
  .brand__name { font-size: 26px; font-weight: 400; letter-spacing: 2px; text-transform: uppercase; }
  .testimonial { position: absolute; right: 80px; top: 938px; text-align: right; }
  .testimonial__title { font-size: 21px; font-weight: 700; line-height: 1.02; }
  .testimonial__title span { display: block; color: var(--cyan); }
  .testimonial__quote { font-size: 16px; line-height: 1.3; margin-top: 8px; }
  .testimonial__quote .mark { color: var(--cyan); }
  .testimonial__source { font-size: 12.5px; font-weight: 700; color: var(--cyan); margin-top: 16px; }
</style>
</head>
<body>
<main class="ad">
  <div class="ad__photo" role="img" aria-label="Aerial photo of a dark ocean meeting a turquoise lagoon, a sandy curved beach and dense palm jungle, with a small wooden boat on the water"></div>
  <div class="ad__shade"></div>

  <h1 class="headline">
    <span class="headline__top">LUXURY</span>
    <span class="headline__bottom">REIMAGINED</span>
  </h1>

  <p class="subhead">Once-in-a-lifetime journeys, designed<br>with <strong>vision, trust, and timeless detail</strong></p>

  <section class="features">
    <div class="feature">
      <h2 class="feature__title">BESPOKE EXPERIENCES</h2>
      <p class="feature__text">Impeccably curated adventures crafted<br>with creativity and care.</p>
    </div>
    <div class="feature">
      <h2 class="feature__title">WHITE-GLOVE SERVICE</h2>
      <p class="feature__text">From first idea to final return, every detail<br>is flawlessly handled.</p>
    </div>
    <div class="feature">
      <h2 class="feature__title">EXPERTISE YOU CAN TRUST</h2>
      <p class="feature__text">38 years of unmatched insight, global<br>connections, and premium access.</p>
    </div>
  </section>

  <div class="cta">
    <p class="cta__script">Let us create your next</p>
    <p class="cta__lead">UNFORGETTABLE ESCAPE</p>
  </div>

  <div class="contact">
    <div class="contact__row">
      <svg class="contact__icon" viewBox="0 0 24 24" fill="none" stroke="#45cfa3" stroke-width="2.2" stroke-linecap="round" stroke-linejoin="round"><path d="M22 16.9v3a2 2 0 0 1-2.2 2 19.8 19.8 0 0 1-8.6-3.1 19.5 19.5 0 0 1-6-6A19.8 19.8 0 0 1 2.1 4.2 2 2 0 0 1 4.1 2h3a2 2 0 0 1 2 1.7c.1 1 .4 1.9.7 2.8a2 2 0 0 1-.5 2.1L8 9.9a16 16 0 0 0 6 6l1.3-1.3a2 2 0 0 1 2.1-.4c.9.3 1.8.6 2.8.7a2 2 0 0 1 1.7 2z"/></svg>
      <span>800.555.0142</span>
    </div>
    <div class="contact__row">
      <svg class="contact__icon" viewBox="0 0 24 24" fill="none" stroke="#45cfa3" stroke-width="2.2"><circle cx="12" cy="12" r="10"/><path d="M2 12h20M12 2a15 15 0 0 1 0 20M12 2a15 15 0 0 0 0 20"/></svg>
      <span>www.tidalreverie-example.com</span>
    </div>
  </div>

  <div class="brand">
    <span class="brand__name">Tidal Reverie</span>
    <span class="brand__mark"></span>
  </div>

  <aside class="testimonial">
    <h3 class="testimonial__title">UNRIVALED<span>REPUTATION</span></h3>
    <p class="testimonial__quote"><span class="mark">“</span>No one does<br>what you do<span class="mark">”</span></p>
    <p class="testimonial__source">Cruise Line Executive</p>
  </aside>
</main>
</body>
</html>
```